Web Design Project

To Create new charity website currently (www.morvalenhope.org)
Please request for full requirements in PDF format via email.
dilan.perow@morvalenhope.org cc: dperow_dp@quillmail.com.au

Im unable to load the project details on this page through add files feature. Please ensure you understand the requirments and use www.brightkinfold.com as a good reference. or guide.

Create Users , Registers a Child for Sponsor, Search for a Child to sponsor byCountry, Town, Age group, Gender, Race, Religion days waiting

Donate, Shop from MHG Store, Events, what we do, Get Involved Category, gallery, Upcoming events.

-Main Focus on Child Sponsor
Online Registeration request for Child Support to MHG Team allow document upload by the registering person.

MHG Team reviews the request checking and verifying all the details including documents submitted
(this will be published after being approved by MHG Committee. once approved then MHG Publishes the details for sponsors

There should be section where highlights are uniquely identified. such as upcoming event or shows, Appeal for Cyclone or Flood Relief or Medical Assistance.
May be scrolling text or something similar.
#Manage community fundraisers and display their information, performance etc. Automated online letter on thanks, support and reminders such as Bdays and payment renewals.

#The addition should consist of online database which tracks upcoming fundraising events, fundraisers, team and donations. Photo and events gallery. Sponsors,
Online ecards, registerations of sponsor, members, volunteers and all internet users who want to receive regular updates.

Registeration database to create users by category (may be)
sponsor, looking for sponsors, volunteers, members, donors, others etc. create registeration and capture info in database
name , dob, gender, country, email add, phone
registeration needs to be verified by email confirmation link send back to email add supplied for verification

1. A fundraising home page with an attractive layout that displays an overview of fundraising events, teams and individuals. This information could be organized by event location, date etc.

2. Event Home page for each fundraising event. We need to tap into our e-commerse setup to allow us to include a) a gauge of how much has been raised so far, b) a list of recent donors and their messages c) a way for people to donate directly to the fundraiser or team member, and d) some sort of blog that the fundraiser themselves can update with pictures and information.

admin page.
number of visits made to web site.
registered members
After its launched it wil be manages by our members,

reference to www.brightkinfold.com/ our members have liked this very much
and also get involved from and shop from http://tarwickaid.org.au/ to get more ideas and use only as a reference to bring user friendliness and efficient elegant look and ease of use to users.

The final product modern and inspire people to get involved and fundraise. and provide online donations and gifts and also shopping benefits through our web site to get discounts to all internet shoppers

Administration Page.

////////////////////////////////////////////////////////////////////////////////////////////
Registeration is required for
for sponsors, Child looking for sponsor, Shopping Donors, Members Volunteers etc

Username / Password
User details name
Name (s) First, Last Middle Address, Suburb/Town, Country, Post Code, +
Land Line: Country Code/Area Code/#
Mobile: Country Code/Number
Password Reset Method via email or secret Q/A at least 2.

Other functions as a registered users of MHG to provide
Account Summary
My Sponsorship
Additional Givings
Write my Child/Sponsor
make a Payment
Account Settings
Payment Options
My Activity
Questions.

I need the Unique identifyiny feature for upcoming event appeal for something that attracts peoples attention.

May be a bold scrolling text such : Morvalen Hope Group has lauched KORALI STORM DRIVE 2013, or Priyanka Medical Assistance Appeal and once a person clicks on the scrolling text get the full details of the appeal and what needs to be done to support. Should not be limited to only 1 appeal but may be upto 512 Characters or some better ways of presenting. eg may be there is appeal, fund raiser, medical assistance etc.

Childs Sponsor and other activity
Register a Child
Search for a Child
Sponsor a Child

Persons willing to register for a chile Online Registration request for Child Support

Name, middle Surname,
Age: 9 (calculated Automatically from DOB)
• Birthday: February 15, 2004 (Drop Down Box_
• Gender: Female (Radio button)
• Country: (select from List)
• Town/City: (select from List)
• Suburb/Village: (User Entry If Doesn’t Exist) Or better approach
• Ethnicity/Race: (User Enter if doesn’t exist) Or better approach
• Religion: (User Enters If doesn’t exist) Or better approach
• Photo
• Child ID: Automatically Generated by System
o Initial Registeration Child ID will be prefixed by letter z. eg z123456
o Once approved and published by MHG Administrator prefix z will be removed. Automatically
MHG Administrator should be able to edit update add or delete any information from maintenance Page or from the database.

o Calculate from date of publishing Child Waiting: 257 Days for a sponsor
o
• Allow Upload of supporting document Document (Any Format for verification)
• Allow upload of Photos (s) max of 3

Registeration MUST
All Person who are looking for Child to support or looking for sponsors or donations charity membership, Volunteers subscribing for new letters and events must register first, Social networking.

TO Register with MHG
Username, password min of 6 max 10, Firstname, Lastname, TownCity, Country, email:
Optional:
Phone: country code, area code number Mobile: Country Code, Mobile number
Every registered person should be able to see all HIS ACTIVITY donations and other details under his profile:

Administration Page
Easy Manageable Admin Page
All step by step guide of updating each and every page
Tools and software must be provided for managing the website.
Easy and efficient way of Managing Pictures Allow single multiple and all images in a folder to be uploaded in simple steps: Able to reset password if required.

Well Structured layout and defined layers links to each and every page. Home button to be available in all pages.

Reports
MHG Admin should be able to generate reports from database such as mysql if any other db used some simple queries or adhoc report to be generated
Eg: All sales in MHG Store by date cateogy amount total sales by country and town grouped by:

Upcoming Events
Allows easy and user friendly interface for updating the pages for upcoming events.
MHG Admin should be able to send email to all registered users with attachments such as news letters, request for support etc etc

Gallery
MHG Admin should be able to able select the default folder to use for Scrolling images
Eg: 1 week I would all sponsored childs folder to be used to scroll all images
2nd week I may default to all events pics
3rd I may select Diaster relief
Or I can use random pics from all folders under gallery
My folder structure for gallery may be like this. I will select where Im uploading photos and then

Gallery
Childs
Disaster
Events
Stores (Note Stores will also have scrolling images for all items listed for sale) and it has to have a tag and stock list or number of items available once it reaches 0 it should be labeled out of stock.

• Create Child ID Automatically and Photos to MHG Team allow document upload by the registering person.

manage community fundraisers and display their information, performance etc. Automated online letter of thanks, support and reminders payment renewals due day and 7 days before due date. Bdays

Additional info that may be useful but not necessary and if it can improve in way to make our web site more attractive and efficient.
During Registeration needs to be verified by email confirmation link send back to email add supplied for verification and the user gets registered

2. Events page for each category fundraising team event.
Sponsor a Child
Micro Enterprise
Social Events
Medical Assitance
Relief & Assistance
IT Projects
Special Projects

We need to tap into our e-commerse setup to allow us to include
a) a gauge of how much has been raised so far, b) a list of recent donors and their messages c) a way for people to donate directly to the fundraiser or team member, and d) some sort of blog that the MHG fundraiser Team Leader themselves can update with pictures and information.

Number of visits made to web site.
Marketing links/ Ads

Example: http://www.brightkinfold.com/
our members have liked this very much
and also
get involved from and shop from
http://tarwickaid.org.au/

Updates

Hi All

I need to complete this project asap. may be in next 4 to 6 weeks maximum

so please submit you design overview, features functionality

thanks

Dilan

                                       

Project Details/Requirements

To Create new charity website currently (www.morvalenhope.org) reference www.brightkinfold.com

 

Create login (for sponsors, Child looking for sponsor, Shopping Donors, Members Volunteers etc

               Username / Password

               User details name

                              Name (s) First, Last Middle Address, Suburb/Town, Country, Post Code,  +

 

Other functions as a registered users of MHG  to provide

Account Summary

My Sponsorship

Additional Givings

Write my Child/Sponsor

make a Payment

Account Settings

Payment Options

My Activity

Questions.

 

Reference to snapshot below

 

 

 

 

 

Change the background colour. Need to have a good search feature for the child. Refer to www.brightkinfold.org web site as a guide pretty much very similar features I need. Also

 

 

               Register a Child

               Search for a Child

               Sponsor a Child

 

 

<!-[if !supportLists]->·        <!-[endif]->Online Registration request for Child Support

<!-[if !supportLists]->·        <!-[endif]->Age: 9  (calculated Automatically from DOB)

<!-[if !supportLists]->·        <!-[endif]->Birthday: February 15, 2004  (Drop Down Box_

<!-[if !supportLists]->·        <!-[endif]->Gender: Female (Radio button)

<!-[if !supportLists]->·        <!-[endif]->Country: (select from List)

<!-[if !supportLists]->·        <!-[endif]->Town/City: (select from List)

<!-[if !supportLists]->·        <!-[endif]->Suburb/Village: (User Entry If Doesn’t Exist) Or better approach

<!-[if !supportLists]->·        <!-[endif]->Ethnicity/Race: (User Enter if doesn’t exist) Or better approach

<!-[if !supportLists]->·        <!-[endif]->Religion: (User Enters If doesn’t exist) Or better approach

<!-[if !supportLists]->·        <!-[endif]->Photo

<!-[if !supportLists]->·        <!-[endif]->Child ID: Automatically Generated by System

<!-[if !supportLists]->o   <!-[endif]->Initial Registeration Child ID will be prefixed by letter z. eg z123456

<!-[if !supportLists]->o   <!-[endif]->Once approved and published by MHG Administrator prefix z will be removed. Automatically

<!-[if !supportLists]->·        <!-[endif]-> 

<!-[if !supportLists]->o   <!-[endif]->Calculate from date of publishing Child Waiting: 257 Days for a sponsor

<!-[if !supportLists]->o   <!-[endif]-> 

<!-[if !supportLists]->·        <!-[endif]->Allow Upload of supporting document Document (Any Format for verification)

<!-[if !supportLists]->·        <!-[endif]->Allow upload of Photos (s) max of 3

 

Registeration MUST

 

TO Register with MHG

Optional:

Phone: country code, area code number  Mobile: Country Code, Mobile number

 

 

 

            

                           

Administration Page

Easy and efficient way of Managing Pictures Allow single multiple and all images in a folder to be uploaded in simple steps

 

              

Reports

 

Upcoming Events

 

Gallery

 

               Gallery

                              Childs

                              Disaster

                              Events

                              Stores  (Note Stores will also have scrolling images for all items listed for sale) and it has to have a tag and stock list or number of items available once it reaches 0 it should be labeled out of stock.

                             

 

 

<!-[if !supportLists]->·        <!-[endif]->Create Child ID Automatically and Photos  to MHG Team allow document    upload by the registering person.

<!-[if !vml]-><!-[endif]->

         MHG Team reviews the request checking and verifying all the details including    documents submitted

        

        

manage community fundraisers and display their information, performance etc. Automated online letter of thanks, support and reminders payment renewals due day and 7 days before due date.  Bdays

 

 

 

Sponsor a Child

                              Micro Enterprise

                              Social Events

                              Medical Assitance

                              Relief & Assistance

                              IT Projects

                              Special Projects

 

                             

 

Marketing links/ Ads

 

 

 

 

and also

http://tarwickaid.org.au/

 

 

 

 

                                   

Target Market(s)

get and attract as many charity supporters as possible

Industry/Entity Type

Internet

Requirements
Must have
• Refer to attached documents
Users manual or step by step guide on how to manage and update web pages.
Nice to have
• nice catchy looks and layout
Reporting online options

```html
<!DOCTYPE html>
<html lang="en">
<head>
<meta charset="utf-8">
<title>Morvalen Hope – Sponsor a Child</title>
<link href="https://fonts.googleapis.com/css2?family=Open+Sans:ital,wght@0,400;0,600;0,700;0,800;1,700&display=swap" rel="stylesheet">
<style>
:root{
  --ink:#1b1b1b;
  --night:#121417;
  --navy:#0c2e5c;
  --blue:#1b6cc0;
  --blue-bright:#2f8fe2;
  --sky:#dcebf8;
  --yellow:#f4c20d;
  --orange:#f08a1c;
  --paper:#ffffff;
  --canvas:#d6d8db;
  --line:#c4c7cc;
  --muted:#5f646b;
}
*{box-sizing:border-box;margin:0;padding:0}
html,body{width:824px;height:1200px;overflow:hidden}
body{font-family:"Open Sans",Arial,sans-serif;color:var(--ink);background:var(--canvas);position:relative;font-size:9px}
a{color:inherit;text-decoration:none}

.site-header{position:absolute;left:0;top:0;width:824px;height:80px;background:radial-gradient(ellipse at 18% 40%,#1d4f8c 0%,var(--night) 55%)}
.brand{position:absolute;left:52px;top:20px;display:flex;align-items:center;gap:10px}
.brand-dot{width:34px;height:34px;border-radius:50%;background:var(--blue-bright)}
.brand-name{font-size:24px;font-weight:800;color:#fff;letter-spacing:.5px}
.utility-links{position:absolute;right:52px;top:8px;display:flex;gap:6px;color:#fff;font-size:8px}
.utility-links span{color:var(--yellow)}

.main-nav{position:absolute;left:52px;top:80px;width:720px;height:26px;display:flex;background:var(--blue)}
.main-nav a{flex:1;color:#fff;font-weight:700;font-size:10px;display:flex;align-items:center;justify-content:center;border-right:1px solid #4d93d6}
.main-nav a.involved{background:var(--yellow);color:var(--ink);flex:.7;border:none}

.hero{position:absolute;left:52px;top:114px;width:508px;height:232px;background:var(--paper);padding:6px}
.hero-photo{width:100%;height:196px;background:linear-gradient(135deg,#8a6b52,#c9a98a 45%,#4f6d8c);position:relative}
.hero-caption{position:absolute;left:0;bottom:0;width:100%;height:34px;background:rgba(0,0,0,.72);color:#fff;font-weight:700;font-size:16px;display:flex;align-items:center;padding-left:12px}
.hero-dots{display:flex;justify-content:center;gap:6px;margin-top:11px}
.hero-dots i{width:8px;height:8px;border-radius:50%;background:#9aa0a6}
.hero-dots i:first-child{background:var(--blue)}

.sidebar{position:absolute;left:568px;top:114px;width:204px}
.cart{background:var(--paper);padding:8px;height:62px}
.panel-title{font-size:11px;font-weight:700;color:var(--ink);margin-bottom:4px}
.cart p{font-size:8px;color:var(--muted);line-height:1.4}
.cart p a{color:var(--blue)}
.child-search{margin-top:6px;background:var(--paper);padding:8px;height:164px}
.child-search .panel-title{font-size:13px}
.field-label{font-size:8px;font-weight:700;margin-top:6px}
.select{height:15px;border:1px solid var(--line);background:#f2f3f4;margin-top:2px;font-size:7px;color:var(--muted);padding:2px 4px;position:relative}
.select:after{content:"";position:absolute;right:4px;top:5px;border:3px solid transparent;border-top-color:#555}
.age-row{display:flex;align-items:center;justify-content:space-between;margin-top:8px}
.age-row .field-label{margin:0}
.btn{display:inline-block;font-size:8px;font-weight:700;color:#fff;background:var(--blue);padding:4px 8px}
.btn.alt{background:var(--yellow);color:var(--ink)}

.card{position:absolute;left:52px;width:720px;background:var(--paper)}
.section-title{color:var(--blue);font-weight:700}
.featured{top:356px;height:56px;padding:6px 10px}
.featured .section-title{font-size:11px}
.badges{display:flex;justify-content:space-between;align-items:center;margin-top:8px}
.badges i{display:block;height:16px;background:#b7bbc1}

.sponsor{top:420px;height:284px;padding:12px}
.sponsor-main{position:absolute;left:12px;top:12px;width:450px}
.sponsor-main .section-title{font-size:22px}
.intro{font-size:8px;color:var(--muted);line-height:1.4;margin-top:4px}
.children{display:flex;gap:14px;margin-top:10px;justify-content:center}
.child-card{width:124px;border:1px solid var(--line)}
.child-name{background:var(--yellow);font-weight:700;font-size:10px;text-align:center;padding:3px 0}
.child-photo{height:90px;background:linear-gradient(160deg,#6b4a36,#b48b6c)}
.child-meta{background:var(--blue);color:#fff;text-align:center;font-size:8px;line-height:1.35;padding:3px 0}
.child-meta b{display:block;font-size:9px}
.cta-row{display:flex;gap:8px;justify-content:center;margin-top:12px}
.news{position:absolute;left:480px;top:12px;width:228px;border-left:1px solid var(--line);padding-left:12px}
.news .section-title{font-size:17px}
.news-item{margin-top:8px}
.news-item h4{font-size:9px;font-weight:700;color:var(--blue)}
.news-item p{font-size:7.5px;color:var(--muted);line-height:1.4;margin-top:2px}
.news-item a{font-size:7.5px;color:var(--blue);font-weight:600}
.news .btn{margin-top:10px}

.distinct{top:712px;height:168px;padding:12px}
.distinct .section-title{font-size:20px;color:var(--ink)}
.distinct .section-title span{color:var(--blue)}
.stats{display:flex;justify-content:space-between;margin-top:14px;padding:0 12px}
.stat{width:200px;height:96px;border:2px solid var(--sky);text-align:center;padding-top:10px}
.stat strong{display:block;font-size:30px;font-weight:800;color:var(--ink)}
.stat p{font-size:8px;color:var(--muted);line-height:1.3;margin-top:2px}
.stat p em{font-style:normal;color:var(--blue);font-weight:700}

.share-bar{position:absolute;left:52px;top:888px;width:720px;height:24px;display:flex;align-items:center;gap:22px;padding:0 12px;font-size:8px;color:var(--muted)}
.share-bar span{display:flex;align-items:center;gap:4px}
.share-bar .socials{margin-left:auto;display:flex;gap:4px}
.share-bar .socials i{width:14px;height:14px;background:var(--blue)}

.site-footer{position:absolute;left:0;top:920px;width:824px;height:246px;background:linear-gradient(var(--blue),var(--navy));color:#fff}
.footer-cols{position:absolute;left:52px;top:18px;display:flex;gap:34px}
.footer-cols ul{list-style:none;font-size:8px;line-height:1.9}
.copyright{position:absolute;right:52px;top:18px;width:190px;font-size:7.5px;line-height:1.6}
.bottom-strip{position:absolute;left:0;top:1166px;width:824px;height:34px;background:var(--night)}
</style>
</head>
<body>

<header class="site-header">
  <div class="brand"><span class="brand-dot"></span><span class="brand-name">Morvalen Hope</span></div>
  <nav class="utility-links"><a>About Us</a><span>|</span><a>Where We Work</a><span>|</span><a>Blog</a><span>|</span><a>My Account</a></nav>
</header>

<nav class="main-nav">
  <a>Sponsor a Child</a><a>Rescue Babies &amp; Mothers</a><a>Develop a Future Leader</a><a>Meet Critical Needs</a><a class="involved">Get Involved</a>
</nav>

<section class="hero">
  <div class="hero-photo" role="img" aria-label="Photo of smiling children in Fiji">
    <div class="hero-caption">Sponsor TWO Children in Fiji Now for only $100 per year!!</div>
  </div>
  <div class="hero-dots"><i></i><i></i><i></i><i></i></div>
</section>

<aside class="sidebar">
  <div class="cart">
    <h3 class="panel-title">Shopping Cart</h3>
    <p>Your shopping cart is empty.<br><a>Visit the shop</a></p>
  </div>
  <div class="child-search">
    <h3 class="panel-title">Search for a Child</h3>
    <div class="field-label">Where in The World</div>
    <div class="select">No Preference</div>
    <div class="field-label">Gender</div>
    <div class="select">No Preference</div>
    <div class="field-label">Age Range: 0 to 22</div>
    <div class="select">Any Age</div>
    <div class="age-row"><span class="field-label">Days Waiting</span><a class="btn alt">Search Now</a></div>
  </div>
</aside>

<section class="card featured">
  <h3 class="section-title">Featured On</h3>
  <div class="badges">
    <i style="width:60px"></i><i style="width:70px"></i><i style="width:50px"></i><i style="width:66px"></i><i style="width:56px"></i><i style="width:74px"></i><i style="width:52px"></i><i style="width:64px"></i>
  </div>
</section>

<section class="card sponsor">
  <div class="sponsor-main">
    <h2 class="section-title">Sponsor a Child</h2>
    <p class="intro">Make a lasting difference in the life of a child in need. Sponsor a child today! When you sponsor a child to provide your sponsored child will be linked. Then you will see how your gift helps them grow, learn and play each day in their own village.</p>
    <div class="children">
      <article class="child-card">
        <div class="child-name">Mereani</div>
        <div class="child-photo" role="img" aria-label="Photo of Mereani"></div>
        <div class="child-meta"><b>Fiji</b>12-04-2003</div>
      </article>
      <article class="child-card">
        <div class="child-name">Losana</div>
        <div class="child-photo" role="img" aria-label="Photo of Losana"></div>
        <div class="child-meta"><b>Fiji</b>03-09-2005</div>
      </article>
      <article class="child-card">
        <div class="child-name">Tevita</div>
        <div class="child-photo" role="img" aria-label="Photo of Tevita"></div>
        <div class="child-meta"><b>Fiji</b>21-06-2004</div>
      </article>
    </div>
    <div class="cta-row"><a class="btn">View More Children</a><a class="btn">Search for Children</a></div>
  </div>
  <div class="news">
    <h2 class="section-title">Latest News</h2>
    <div class="news-item">
      <h4>Fiji Flood Relief Appeal</h4>
      <p>Morvalen Hope Group - Fiji Flood Relief Appeal. Flood victims lost stationery bought for school children and books they had. School time has already started.</p>
      <a>Read More</a>
    </div>
    <div class="news-item">
      <h4>Yacata Nursing Stations &amp; Samoa Health Centre Water Tanks</h4>
      <p>Morvalen Hope Group is a child focus non profit seeking to fund a nursing station and health centre water tanks for the local villages.</p>
      <a>Read More</a>
    </div>
    <a class="btn alt">Read All</a>
  </div>
</section>

<section class="card distinct">
  <h2 class="section-title">What Makes Morvalen <span>Hope</span> Distinct</h2>
  <div class="stats">
    <div class="stat"><strong>163,527</strong><p>kids &amp; moms have united <em>below</em><br>in the fight for hope last year</p></div>
    <div class="stat"><strong>5,659</strong><p>International<br>Church Partners</p></div>
    <div class="stat"><strong>1,163,527</strong><p>Currently<br>our Sponsor Children</p></div>
  </div>
</section>

<div class="share-bar">
  <span>&#9993; Email a friend</span><span>&#10003; Subscribe</span><span>&#43; Bookmark &amp; Share</span><span>&#9113; Print this Page</span>
  <span class="socials"><i></i><i></i><i></i></span>
</div>

<footer class="site-footer">
  <div class="footer-cols">
    <ul><li>Sponsor a Child</li><li>Rescue Babies &amp; Mothers</li><li>Develop a Future Leader</li><li>Meet Critical Needs</li><li>Donate Now</li><li>Get Involved</li></ul>
    <ul><li>Employment Opportunities</li><li>Press Center</li><li>Contact Us</li><li>Get Involved</li><li>Children &amp; Poverty</li><li>About Us</li></ul>
    <ul><li>Blog</li><li>Where We Work</li><li>My Account</li><li>Support Network</li><li>Morvalen Hope FAQ</li><li>Site Map</li></ul>
  </div>
  <div class="copyright">© 2013 Morvalen Hope. All Rights Reserved.<br>Privacy Statement and Conditions of Use. Safe Our Personal Statement.<br>Morvalen Hope is a registered not for profit organization.<br>All donations to the United States are tax deductible to full to gift.</div>
</footer>
<div class="bottom-strip"></div>

</body>
</html>
```